Business Cards

Front page logo Centered with my pic pointing to the logo
quote "Your Home Loan Source"
A Licensed Mortgage Broker Business
equal housing symbol underneath left corner-lime green like logo
Towards right side Calvin R. Mendez
President NMLS #594207
4183 CR 29B Suite 2046517
Lake Mary, FL 32819
Cell: 407-381-5920
Fax: 407-317-8452
Cmendez@quillnet.example
www.MendezLoanPartners.example
Back page of card I want the logo to cover the whole card with a slogan
"Our Associates will meet all your Mortgage, Financial, Real Estate, Legal, Insurance & Title Needs"
Don't forget to go to our website and click on the Associates Tab!
Target Market(s)
People who need a mortgage or real estate needs
Industry/Entity Type
Business
Contact Information for Business Card
see under project description
Font styles to use
Other font styles liked:
- what logo script is
Requirements
Nice to have
- see under project description
Should not have

```html
<!DOCTYPE html>
<html lang="en">
<head>
<meta charset="utf-8">
<title>Mendez Loan Partners – Business Cards</title>
<link rel="stylesheet" href="https://fonts.googleapis.com/css2?family=Open+Sans:wght@400;600;700&display=swap">
<style>
  :root {
    --stage: #e9e7e3;
    --card-dark: #232726;
    --card-dark-2: #2e3331;
    --lime: #8fd12b;
    --lime-light: #b9ea5c;
    --ink: #1d201f;
    --ink-soft: #3c4240;
    --paper: #e8e6e1;
    --muted: #b7bab6;
  }
  * { box-sizing: border-box; margin: 0; padding: 0; }
  html, body { width: 1200px; height: 1023px; overflow: hidden; }
  body {
    background: var(--stage);
    font-family: "Open Sans", Arial, sans-serif;
    position: relative;
  }
  .card {
    position: absolute;
    width: 620px;
    height: 354px;
    border-radius: 6px;
    overflow: hidden;
    background: var(--card-dark);
    box-shadow: 0 10px 24px rgba(0,0,0,.25);
  }
  .card--front { left: 70px; top: 90px; }
  .card--back { left: 510px; top: 570px; background: linear-gradient(135deg, var(--card-dark-2), var(--card-dark)); }

  /* front */
  .front-panel { position: absolute; inset: 0; }
  .front-top {
    position: absolute; left: 0; right: 0; top: 0; height: 36px;
    display: flex; align-items: center; justify-content: flex-end;
    padding-right: 22px;
    color: var(--lime); font-size: 12px; font-weight: 600;
  }
  .photo-area {
    position: absolute; left: 130px; top: 172px; width: 230px; height: 138px;
    background: linear-gradient(160deg, #6f6a64 0%, #4a4643 55%, #d9dcdf 100%);
  }
  .front-logo {
    position: absolute; left: 22px; top: 66px; width: 276px; text-align: center;
  }
  .brand {
    display: inline-flex; align-items: center; gap: 7px;
    color: var(--lime); font-weight: 700; font-size: 17px; line-height: 1.15;
    text-transform: uppercase; letter-spacing: .3px; white-space: nowrap;
  }
  .brand__mark { width: 12px; height: 12px; background: var(--lime); flex: none; }
  .brand__sub { display: block; color: var(--lime); font-weight: 700; font-size: 10px; letter-spacing: 1.5px; text-transform: uppercase; margin-top: 3px; }
  .tagline {
    margin: 8px auto 0; width: 210px; border-top: 1.5px solid var(--muted);
    padding-top: 5px; color: var(--paper); font-size: 10px; letter-spacing: 1.8px; text-transform: uppercase; white-space: nowrap;
  }
  .contact {
    position: absolute; right: 22px; top: 54px; text-align: right; color: var(--ink);
  }
  .contact__name { font-size: 19px; font-weight: 700; text-transform: uppercase; letter-spacing: .5px; }
  .contact__role { font-size: 11px; color: var(--ink-soft); margin-bottom: 12px; }
  .contact__line { font-size: 12px; display: flex; align-items: center; justify-content: flex-end; gap: 6px; margin-top: 6px; }
  .contact__icon { width: 12px; height: 12px; }
  .front-bottom {
    position: absolute; left: 0; right: 0; bottom: 0; height: 44px;
    display: flex; align-items: center; justify-content: space-between; padding: 0 22px;
    color: var(--paper); font-size: 11px;
  }
  .licensed { display: flex; align-items: center; gap: 8px; color: var(--lime); }
  .housing-badge { width: 18px; height: 18px; border: 2px solid var(--lime); }
  .address { font-weight: 700; }

  /* back */
  .back-content {
    position: absolute; inset: 0; display: flex; flex-direction: column; align-items: center; justify-content: center; text-align: center;
  }
  .brand--large { font-size: 30px; gap: 8px; }
  .brand--large .brand__mark { width: 20px; height: 20px; }
  .brand--large + .brand__sub { font-size: 15px; letter-spacing: 3px; }
  .back-rule { width: 300px; border-top: 1.5px solid var(--muted); margin: 12px 0 12px; }
  .slogan { color: var(--paper); font-size: 13px; line-height: 1.5; max-width: 470px; }
  .reminder { color: var(--lime); font-size: 12px; margin-top: 12px; }
  .back-web { color: var(--lime); font-size: 13px; font-weight: 700; margin-top: 4px; }
</style>
</head>
<body>

<section class="card card--front" aria-label="Business card front">
  <svg class="front-panel" width="620" height="354" viewBox="0 0 620 354" aria-hidden="true">
    <defs>
      <linearGradient id="limePanel" x1="0" y1="0" x2="1" y2="1">
        <stop offset="0" stop-color="#c4ef6e"/>
        <stop offset="1" stop-color="#7fc41e"/>
      </linearGradient>
    </defs>
    <polygon points="360,36 620,36 620,310 210,310" fill="url(#limePanel)"/>
    <line x1="360" y1="36" x2="210" y2="310" stroke="#8fd12b" stroke-width="4"/>
  </svg>

  <div class="front-top">www.MendezLoanPartners.example</div>

  <div class="photo-area" role="img" aria-label="Portrait photo of Calvin R. Mendez pointing up toward the logo"></div>

  <div class="front-logo">
    <span class="brand"><span class="brand__mark"></span>Mendez Loan Partners</span>
    <span class="brand__sub">&amp; Associates LLC</span>
    <p class="tagline">Your Home Loan Source</p>
  </div>

  <div class="contact">
    <p class="contact__name">Calvin R. Mendez</p>
    <p class="contact__role">President | NMLS #594207</p>
    <p class="contact__line">407-381-5920
      <svg class="contact__icon" viewBox="0 0 12 12" aria-label="Cell"><rect width="12" height="12" rx="2" fill="#1d201f"/><rect x="4" y="2" width="4" height="8" rx="1" fill="none" stroke="#b9ea5c"/></svg></p>
    <p class="contact__line">407-317-8452
      <svg class="contact__icon" viewBox="0 0 12 12" aria-label="Fax"><rect width="12" height="12" rx="2" fill="#1d201f"/><rect x="2.5" y="4" width="7" height="5" fill="none" stroke="#b9ea5c"/></svg></p>
    <p class="contact__line">Cmendez@quillnet.example
      <svg class="contact__icon" viewBox="0 0 12 12" aria-label="Email"><rect width="12" height="12" rx="2" fill="#1d201f"/><path d="M2.5 3.5h7v5h-7z M2.5 3.5 6 6.5 9.5 3.5" fill="none" stroke="#b9ea5c"/></svg></p>
  </div>

  <div class="front-bottom">
    <span class="licensed"><span class="housing-badge" role="img" aria-label="Equal housing badge"></span>A Licensed Mortgage Broker Business</span>
    <span class="address">4183 CR 29B Suite 2046517, Lake Mary, FL 32819</span>
  </div>
</section>

<section class="card card--back" aria-label="Business card back">
  <div class="back-content">
    <span class="brand brand--large"><span class="brand__mark"></span>Mendez Loan Partners</span>
    <span class="brand__sub">&amp; Associates LLC</span>
    <div class="back-rule"></div>
    <p class="slogan">Our Associates will meet all your<br>Mortgage, Financial, Real Estate, Legal, Insurance &amp; Title Needs</p>
    <p class="reminder">Don't forget to go to our website and click on the Associates Tab!</p>
    <p class="back-web">www.MendezLoanPartners.example</p>
  </div>
</section>

</body>
</html>
```